Design my Display Ad! Product for Muscle Cramps -- Need Your Talent!

I need the PSD of a square display ad to be the design concept for other ad formats. The product is for leg and muscle cramps. The ad needs to encourage clicks, not simply impressions. Image should contain legs.

Visit www.legsoothewell.com for a better idea of the product.

Target Market(s)

People age 55+ with leg cramps

Industry/Entity Type

Health And Wellness

Font styles to use
Sans Serif

Colors

Designer to choose colors to be used in the design.

Requirements
Must have
• One version with the text:
• The Real Cause of Leg Cramps
• Discover the Secret
• The other version with the text:
• Leg Cramps at Night
• Discover the Real Cause
• An image focused on legs.
• Attractive presentation -- this is a premium organic brand.
• Visit www.legsoothewell.com for a better understanding of the product

```html
<!DOCTYPE html>
<html lang="en">
<head>
<meta charset="utf-8">
<title>Leg Cramps at Night – Display Ad</title>
<link rel="stylesheet" href="https://fonts.googleapis.com/css2?family=Montserrat:wght@300;700&display=swap">
<style>
  :root {
    --field-green: #9fb53f;
    --light-green: #b6cd55;
    --badge-blue: #4fa8dc;
    --ink-white: #ffffff;
    --silhouette: #141414;
  }
  html, body {
    margin: 0;
    padding: 0;
    width: 1200px;
    height: 1200px;
    overflow: hidden;
    background: var(--field-green);
  }
  .ad {
    position: relative;
    width: 1200px;
    height: 1200px;
    overflow: hidden;
    font-family: "Montserrat", sans-serif;
  }
  .ad-art {
    position: absolute;
    inset: 0;
    width: 1200px;
    height: 1200px;
  }
  .headline-strong {
    font-family: "Montserrat", sans-serif;
    font-weight: 700;
    fill: var(--ink-white);
  }
  .headline-light {
    font-family: "Montserrat", sans-serif;
    font-weight: 300;
    fill: var(--ink-white);
  }
  .cta-text {
    font-family: "Montserrat", sans-serif;
    font-weight: 300;
    fill: var(--ink-white);
  }
  .motion-line {
    stroke: var(--silhouette);
    stroke-width: 7;
    stroke-linecap: butt;
  }
</style>
</head>
<body>
<main class="ad">
  <svg class="ad-art" viewBox="0 0 1200 1200" xmlns="http://www.w3.org/2000/svg">
    <rect class="background" x="0" y="0" width="1200" height="1200" fill="var(--field-green)"/>
    <polygon class="background-wedge" points="0,60 435,1200 0,1200" fill="var(--light-green)"/>

    <text class="headline-strong" x="1092" y="165" font-size="134" text-anchor="end" textLength="915" lengthAdjust="spacingAndGlyphs">LEG CRAMPS</text>
    <text class="headline-light" x="1092" y="338" font-size="152" text-anchor="end" textLength="920" lengthAdjust="spacing">AT NIGHT</text>

    <rect class="leg-illustration" x="770" y="380" width="360" height="770" rx="40" fill="var(--silhouette)" role="img" aria-label="Black silhouette of a cramping leg, bent at the knee with the foot pointed"/>

    <line class="motion-line" x1="665" y1="777" x2="776" y2="792"/>
    <line class="motion-line" x1="700" y1="915" x2="804" y2="873"/>
    <line class="motion-line" x1="764" y1="1035" x2="843" y2="957"/>

    <a class="cta-badge" href="#">
      <circle cx="320" cy="860" r="260" fill="var(--badge-blue)"/>
      <text class="cta-text" x="320" y="808" font-size="74" text-anchor="middle" textLength="378" lengthAdjust="spacingAndGlyphs">DISCOVER</text>
      <text class="cta-text" x="320" y="904" font-size="74" text-anchor="middle" textLength="378" lengthAdjust="spacingAndGlyphs">THE REAL</text>
      <text class="cta-text" x="320" y="1000" font-size="74" text-anchor="middle" textLength="250" lengthAdjust="spacingAndGlyphs">CAUSE</text>
    </a>
  </svg>
</main>
</body>
</html>
```